Tolvane Air Center needs a new upscale business card design for our high end aircraft hangar complex

Tolvane Air Center (TAC) is a large, upscale jet hangar complex in the US housing expensive aircraft. We need a new business card design, using our current logo. We will be attending a industry convention and need a card design that will stand out and be remembered by aircraft owners and private pilots.

Target Market(s)

Aircraft pilots or owners looking for a new upscale hangar

Industry/Entity Type

Airport

I like to use very heavy card stock, 400#, double sided. Square, no rounded edges please.

Colors
3276b5
0255a3
85abd2

Requirements
Must have
• An expensive, classy design, vivid colors.
Nice to have
• Needs to look very expensive and classy, and have some "pop". Designer must be able to download or copy my current typeface or fonts.
• One card side might be black with the "Logo and Tolvane Air Center Double line image in blue (or try gold, or glossy black), and perhaps have a grayed out "R470 jet silhouette". The other card side would have our contact info, and perhaps the "TAC Logo only". I'd like my contact info 'stacked', not in a paragraph format.
Should not have
• Should not look "too busy". Having a double-sided card will help.

```html
<!DOCTYPE html>
<html lang="en">
<head>
<meta charset="utf-8">
<title>Tolvane Air Center – Business Card</title>
<link rel="stylesheet" href="https://fonts.googleapis.com/css2?family=Montserrat:wght@400;500;700;800&display=swap">
<style>
  :root {
    --backdrop: #2b2b2d;
    --card-blue: #2a72a8;
    --card-white: #ffffff;
    --ink-navy: #1d3f6f;
    --ink-blue: #3276b5;
    --ink-text: #1f3d63;
    --rule: #2c4c78;
  }
  * { box-sizing: border-box; margin: 0; padding: 0; }
  html, body {
    width: 1200px;
    height: 900px;
    overflow: hidden;
    background: var(--backdrop);
    font-family: "Montserrat", sans-serif;
  }
  .sheet {
    width: 1200px;
    height: 900px;
    display: flex;
    flex-direction: column;
    align-items: center;
    justify-content: center;
    gap: 40px;
  }
  .card {
    width: 700px;
    height: 400px;
    border-radius: 0;
    position: relative;
    overflow: hidden;
  }
  .card--front {
    background: var(--card-blue);
    display: flex;
    align-items: center;
    justify-content: center;
  }
  .brand-name {
    font-weight: 800;
    text-transform: uppercase;
    letter-spacing: 1px;
    line-height: 1.1;
    text-align: center;
    white-space: nowrap;
  }
  .card--front .brand-name {
    color: var(--card-white);
    font-size: 40px;
  }
  .card--back {
    background: var(--card-white);
  }
  .card--back .brand {
    position: absolute;
    left: 50px;
    top: 30px;
    width: 290px;
    height: 340px;
    display: flex;
    align-items: center;
    justify-content: center;
  }
  .card--back .brand-name {
    color: var(--ink-navy);
    font-size: 32px;
  }
  .divider {
    position: absolute;
    left: 365px;
    top: 120px;
    width: 1.5px;
    height: 170px;
    background: var(--rule);
  }
  .contact {
    position: absolute;
    left: 400px;
    top: 112px;
  }
  .contact-name {
    font-weight: 700;
    font-size: 24px;
    color: var(--ink-navy);
  }
  .contact-role {
    font-size: 15px;
    color: var(--ink-blue);
    margin-top: 2px;
    margin-bottom: 16px;
  }
  .contact-list { list-style: none; }
  .contact-list li {
    display: flex;
    align-items: center;
    gap: 10px;
    font-size: 15px;
    color: var(--ink-text);
    line-height: 26px;
    white-space: nowrap;
  }
  .contact-list svg {
    width: 13px;
    height: 13px;
    fill: none;
    stroke: var(--ink-blue);
    stroke-width: 2;
    flex: none;
  }
</style>
</head>
<body>
  <main class="sheet">
    <section class="card card--front">
      <p class="brand-name">Tolvane<br>Air Center</p>
    </section>

    <section class="card card--back">
      <div class="brand">
        <p class="brand-name">Tolvane<br>Air Center</p>
      </div>
      <div class="divider"></div>
      <div class="contact">
        <h1 class="contact-name">Marten Colby</h1>
        <p class="contact-role">Director</p>
        <ul class="contact-list">
          <li>
            <svg viewBox="0 0 24 24"><path d="M5 3h4l2 5-3 2a11 11 0 0 0 6 6l2-3 5 2v4a2 2 0 0 1-2 2A18 18 0 0 1 3 5a2 2 0 0 1 2-2z"/></svg>
            +033 5190-4432
          </li>
          <li>
            <svg viewBox="0 0 24 24"><path d="M3 9c0-3 18-3 18 0v2h-5V9H8v2H3z"/><rect x="5" y="13" width="14" height="8" rx="2"/></svg>
            +033 5170-2281
          </li>
          <li>
            <svg viewBox="0 0 24 24"><rect x="3" y="5" width="18" height="14" rx="2"/><path d="M3 7l9 6 9-6"/></svg>
            info@tolvaneaircenter.com
          </li>
          <li>
            <svg viewBox="0 0 24 24"><circle cx="12" cy="12" r="9"/><path d="M3 12h18M12 3c3 3 3 15 0 18M12 3c-3 3-3 15 0 18"/></svg>
            www.tolvaneaircenter.com
          </li>
        </ul>
      </div>
    </section>
  </main>
</body>
</html>
```